New "above the fold" design for our website

We would like to see some new creative designs for our above the fold section on our homepage. We are an online marketplace for fresh produce and meat.

You must design the desktop and mobile layouts.

Target Market(s)

Women 30-45 years old who buy groceries, with 2 children under 10 years old.

Industry/Entity Type

Grocery Store

Number of Pages Required

1 page

Font styles to use
Sans Serif

Requirements
Must have
• Give customers the sense of organic and farm fresh as we are battling the big supermarket chains.
Nice to have
• Pictures of produce. Pictures of farmers.

```html
<!DOCTYPE html>
<html lang="en">
<head>
<meta charset="utf-8">
<title>Meatwright – Online Butcher</title>
<link rel="stylesheet" href="https://fonts.googleapis.com/css2?family=Montserrat:wght@400;500;600;700&family=Arimo:wght@400;700&display=swap">
<style>
  :root {
    --page-bg: #ffffff;
    --login-red: #e5191f;
    --nav-bg: rgba(255, 255, 255, 0.86);
    --nav-text: #3a3a3a;
    --brand-green: #4f6b3a;
    --headline: #5d5f35;
    --stat-text: #4a4a4a;
    --orange: #f7892b;
    --teal: #4cbf97;
    --yellow: #e9ae2d;
    --green: #8cc63f;
    --accent: #ffe04a;
    --button-yellow: #f5c332;
    --white: #ffffff;
  }
  * { box-sizing: border-box; margin: 0; padding: 0; }
  html, body { width: 1200px; height: 566px; overflow: hidden; background: var(--page-bg); }
  body { position: relative; font-family: "Montserrat", sans-serif; }

  .hero {
    position: absolute; left: 0; top: 0; width: 1200px; height: 509px;
    background:
      radial-gradient(ellipse at 60% 30%, #f2f3c8 0%, rgba(242,243,200,0) 45%),
      radial-gradient(ellipse at 85% 20%, #cfe08a 0%, rgba(207,224,138,0) 50%),
      linear-gradient(120deg, #9cb556 0%, #c7d47c 40%, #b8cf6a 70%, #7fa046 100%);
  }
  .hero-butcher {
    position: absolute; left: 14px; top: 0; width: 376px; height: 509px;
    background: linear-gradient(180deg, rgba(224,196,170,0.55) 0%, rgba(240,240,240,0.6) 40%, rgba(40,52,96,0.55) 100%);
    border-radius: 120px 120px 0 0;
  }
  .hero-produce {
    position: absolute; left: 480px; top: 178px; width: 720px; height: 331px;
    background: linear-gradient(160deg, rgba(196,60,70,0) 0%, rgba(196,60,70,0.75) 35%, rgba(180,40,52,0.85) 70%, rgba(214,180,130,0.8) 100%);
    border-radius: 220px 60px 0 0;
  }

  .login {
    position: absolute; left: 792px; top: 15px; width: 124px; height: 27px;
    background: var(--login-red); color: var(--white);
    font-size: 11px; font-weight: 600; letter-spacing: 0.4px;
    display: flex; align-items: center; justify-content: center; border-radius: 3px;
  }
  .search {
    position: absolute; left: 922px; top: 14px; width: 31px; height: 31px;
    border-radius: 50%; background: rgba(255,255,255,0.75);
    display: flex; align-items: center; justify-content: center;
  }

  .main-nav {
    position: absolute; left: 249px; top: 54px; width: 705px; height: 51px;
    background: var(--nav-bg);
  }
  .main-nav .stripe { position: absolute; bottom: 0; height: 3px; }
  .main-nav a {
    position: absolute; top: 19px; transform: translateX(-50%);
    font-size: 11.5px; font-weight: 600; color: var(--nav-text);
    text-decoration: none; letter-spacing: 0.2px; white-space: nowrap;
  }
  .main-nav .brand-name {
    position: absolute; left: 351px; top: 14px; transform: translateX(-50%);
    font-size: 19px; font-weight: 600; letter-spacing: 1.6px;
    color: var(--brand-green); white-space: nowrap;
  }

  .headline {
    position: absolute; left: 0; top: 138px; width: 1152px; text-align: center;
    font-size: 34px; font-weight: 400; color: var(--headline); letter-spacing: 0.4px;
  }

  .slide-arrow { position: absolute; top: 224px; width: 28px; height: 60px; }
  .slide-arrow.prev { left: 31px; }
  .slide-arrow.next { left: 1131px; }

  .stats {
    position: absolute; left: 249px; top: 350px; width: 702px; height: 28px;
    background: var(--white);
  }
  .stat {
    position: absolute; top: 0; height: 28px; display: flex; align-items: center; gap: 8px;
    font-size: 12px; font-weight: 500; color: var(--stat-text); white-space: nowrap;
  }

  .feature { position: absolute; top: 378px; height: 188px; color: var(--white); }
  .feature.price { left: 249px; width: 176px; background: var(--orange); }
  .feature.delivery { left: 425px; width: 175px; background: var(--teal); }
  .feature.fresh { left: 600px; width: 174px; background: var(--yellow); }
  .feature.organic { left: 774px; width: 177px; background: var(--green); }
  .feature h2 {
    position: absolute; left: 18px; top: 11px;
    font-size: 24px; font-weight: 700; line-height: 1; white-space: nowrap;
  }
  .feature .sub {
    position: absolute; left: 19px; top: 38px;
    font-size: 19px; font-weight: 500; color: var(--accent); white-space: nowrap;
  }
  .feature p {
    position: absolute; left: 23px; top: 78px; width: 148px;
    font-family: "Arimo", sans-serif; font-size: 11px; line-height: 15.5px;
  }
  .feature .more {
    position: absolute; left: 24px; top: 164px;
    font-family: "Arimo", sans-serif; font-size: 11px; font-weight: 700;
  }
  .feature.delivery .lead {
    position: absolute; left: 19px; top: 77px;
    font-family: "Arimo", sans-serif; font-size: 12.5px; line-height: 1.2; white-space: nowrap;
  }
  .feature.delivery .lead-caps {
    position: absolute; left: 19px; top: 97px;
    font-family: "Arimo", sans-serif; font-size: 11px; letter-spacing: 0.1px; white-space: nowrap;
  }
  .postcode {
    position: absolute; left: 20px; top: 124px; width: 146px; height: 20px;
    border: 1px solid rgba(255,255,255,0.85); padding-left: 7px;
    font-family: "Arimo", sans-serif; font-size: 10.5px; line-height: 18px; color: rgba(255,255,255,0.9);
  }
  .shop-now {
    position: absolute; left: 20px; top: 152px; width: 77px; height: 21px;
    background: var(--button-yellow); color: var(--white);
    font-family: "Arimo", sans-serif; font-size: 11px; letter-spacing: 0.4px;
    display: flex; align-items: center; justify-content: center;
  }
</style>
</head>
<body>
  <div class="hero" role="img" aria-label="Blurred green garden background"></div>
  <div class="hero-butcher" role="img" aria-label="Smiling butcher in a striped apron with arms crossed"></div>
  <div class="hero-produce" role="img" aria-label="Cuts of raw red meat with parsley, chilli and garlic on a wooden board"></div>

  <div class="login">LOGIN/REGISTER</div>
  <div class="search">
    <svg width="12" height="12" viewBox="0 0 12 12" aria-hidden="true">
      <circle cx="5" cy="5" r="3.6" fill="none" stroke="#555" stroke-width="1.6"/>
      <line x1="7.6" y1="7.6" x2="11" y2="11" stroke="#555" stroke-width="1.8" stroke-linecap="round"/>
    </svg>
  </div>

  <nav class="main-nav">
    <span class="stripe" style="left:0;width:182px;background:var(--orange)"></span>
    <span class="stripe" style="left:182px;width:109px;background:var(--teal)"></span>
    <span class="stripe" style="left:291px;width:261px;background:#b9b9b9"></span>
    <span class="stripe" style="left:552px;width:80px;background:var(--yellow)"></span>
    <span class="stripe" style="left:632px;width:73px;background:var(--green)"></span>
    <a href="#" style="left:72px">HOW IT WORKS</a>
    <a href="#" style="left:189px">ABOUT US</a>
    <span class="brand-name">MEATWRIGHT</span>
    <a href="#" style="left:521px">PRODUCTS</a>
    <a href="#" style="left:642px">CONTACT</a>
  </nav>

  <h1 class="headline">Organic and Ethically Farmed Meat</h1>

  <svg class="slide-arrow prev" viewBox="0 0 28 60" aria-label="Previous slide">
    <polyline points="26,1 2,30 26,59" fill="none" stroke="#ffffff" stroke-width="2"/>
  </svg>
  <svg class="slide-arrow next" viewBox="0 0 28 60" aria-label="Next slide">
    <polyline points="2,1 26,30 2,59" fill="none" stroke="#ffffff" stroke-width="2"/>
  </svg>

  <div class="stats">
    <div class="stat" style="left:28px">
      <svg width="18" height="18" viewBox="0 0 18 18" aria-hidden="true">
        <rect x="4" y="7" width="10" height="10" fill="var(--orange)"/>
        <rect x="7" y="1" width="4" height="6" fill="var(--orange)"/>
        <rect x="1" y="9" width="3" height="3" fill="var(--orange)"/>
        <rect x="14" y="9" width="3" height="3" fill="var(--orange)"/>
      </svg>
      34500 ORDERS
    </div>
    <div class="stat" style="left:196px">
      <svg width="19" height="19" viewBox="0 0 19 19" aria-hidden="true">
        <path d="M1 9 H15 L13 18 H3 Z" fill="var(--teal)"/>
        <circle cx="15" cy="4" r="3" fill="none" stroke="var(--teal)" stroke-width="1.6"/>
      </svg>
      10093 CUSTOMERS
    </div>
    <div class="stat" style="left:384px">
      <svg width="17" height="17" viewBox="0 0 17 17" aria-hidden="true">
        <rect x="1" y="7" width="3" height="9" fill="var(--yellow)"/>
        <path d="M5 7 L9 1 Q11 1 10.5 4 L10 6.5 H15 Q16.5 7 16 9 L14.5 15 Q14 16 12.5 16 H5 Z" fill="var(--yellow)"/>
      </svg>
      10277 LIKES
    </div>
    <div class="stat" style="left:538px">
      <svg width="16" height="16" viewBox="0 0 16 16" aria-hidden="true">
        <rect x="1" y="1" width="14" height="14" fill="var(--green)"/>
      </svg>
      4430 FOLLOWERS
    </div>
  </div>

  <section class="feature price">
    <h2>Best Price</h2>
    <div class="sub">Always</div>
    <p>Corporis suscipit laboriosam, nisi ut aliquid ex ea commodi cons equat ur, Quis autemvel illum qui dolorem</p>
    <div class="more">Read More &nbsp;›</div>
  </section>

  <section class="feature delivery">
    <h2>Delivery</h2>
    <div class="sub">Quick</div>
    <div class="lead">Quality Meat &amp; Produce</div>
    <div class="lead-caps">DELIVERED TO YOUR DOOR</div>
    <div class="postcode">Enter postcode</div>
    <div class="shop-now">SHOP NOW</div>
  </section>

  <section class="feature fresh">
    <h2>Farm Fresh</h2>
    <div class="sub">Quality</div>
    <p>Nam libero tempore, cum soluta nobis est eligendi optio cumque nihil impedit quo minus id quod maxime</p>
    <div class="more">Read More &nbsp;›</div>
  </section>

  <section class="feature organic">
    <h2>Organic</h2>
    <div class="sub">100% Healthy</div>
    <p>Accusamus et iusto odio dignissimos ducimus qui blanditiis praesentium voluptatum deleniti</p>
    <div class="more">Read More &nbsp;›</div>
  </section>
</body>
</html>
```